Growing Into a Fearless Young Competitor

I am making an athlete version of the book cover that you created before. I need a few modifications to the book, to differentiate the covers. I am not sure what I am looking for, but I would want some fom of "Athlete Version" of this book to differentiate from the parent addition I created before.

Target Market(s)

Female Athletes between 14-22, Parents of Female Athletes 12-22

Font styles to use
Sans Serif

Requirements
Must have
• The same vibe as the previous book cover. I need some differentiation, but keeping the same theme

```html
<!DOCTYPE html>
<html lang="en">
<head>
<meta charset="utf-8">
<title>Growing Into a Fearless Young Competitor – Athlete Edition Cover</title>
<link href="https://fonts.googleapis.com/css2?family=Oswald:wght@500;600&family=Six+Caps&family=Montserrat:wght@400;600;700&family=Questrial&display=swap" rel="stylesheet">
<style>
  :root{
    --stage:#2b2b2b;
    --cover:#0b0b0b;
    --ink:#f2f2f2;
    --ink-soft:#d8d8d8;
    --gold-light:#e3c77a;
    --gold:#c9a34e;
    --gold-dark:#8d6d2a;
    --photo-hi:#9a9a94;
    --photo-mid:#4a4a46;
  }
  *{margin:0;padding:0;box-sizing:border-box}
  html,body{width:1200px;height:1001px;overflow:hidden;background:var(--stage)}
  .cover{position:absolute;left:0;top:67px;width:1200px;height:866px;background:var(--cover);overflow:hidden;color:var(--ink)}
  .athlete-photo{position:absolute;left:330px;top:0;width:870px;height:866px;
    background:
      radial-gradient(ellipse 38% 30% at 62% 48%, rgba(180,160,100,.35), transparent 70%),
      radial-gradient(ellipse 55% 60% at 68% 42%, var(--photo-hi), var(--photo-mid) 45%, transparent 78%);
    opacity:.75}
  .gold{background:linear-gradient(180deg,var(--gold-light) 0%,var(--gold) 45%,var(--gold-dark) 100%);
    -webkit-background-clip:text;background-clip:text;color:transparent}

  /* back cover */
  .back{position:absolute;left:0;top:0;width:574px;height:866px}
  .title-block{position:absolute;text-align:center}
  .title-kicker,.title-tail{font-family:"Oswald",sans-serif;font-weight:600;text-transform:uppercase;color:var(--ink);white-space:nowrap}
  .title-main{font-family:"Six Caps",sans-serif;line-height:.82;text-transform:uppercase}
  .back .title-block{left:150px;width:290px;top:30px}
  .back .title-kicker{font-size:22px;letter-spacing:5px;line-height:22px}
  .back .title-main{font-size:150px;margin-top:2px}
  .back .title-tail{font-size:19px;letter-spacing:3.5px;line-height:20px;margin-top:2px}
  .blurb{position:absolute;left:42px;width:496px;top:214px;font-family:"Questrial",sans-serif;font-size:13px;line-height:16px;color:var(--ink-soft);text-align:justify}
  .blurb p{margin-bottom:14px}
  .blurb strong{font-family:"Montserrat",sans-serif;font-weight:700;color:var(--ink)}
  .about-heading{position:absolute;left:42px;width:496px;top:420px;display:flex;align-items:center;gap:10px;font-family:"Montserrat",sans-serif;font-weight:600;font-size:14px;color:var(--gold)}
  .about-heading::before,.about-heading::after{content:"";flex:1;height:1.5px;background:var(--gold)}
  .author-photo{position:absolute;left:42px;top:454px;width:136px;height:139px;background:radial-gradient(circle at 55% 40%,#6b5a4c,#2a2624 60%,#151515)}
  .bio{position:absolute;left:42px;top:452px;width:496px;font-family:"Questrial",sans-serif;font-size:12.6px;line-height:17.3px;color:var(--ink-soft);text-align:justify}
  .bio .wrap{float:left;width:146px;height:148px}
  .bio p{margin-bottom:12px}
  .brand{position:absolute;left:30px;top:740px;width:160px;text-align:center}
  .brand-dot{width:48px;height:48px;border:2px solid var(--gold);border-radius:50%;margin:0 auto 8px}
  .brand-name{font-family:"Montserrat",sans-serif;font-weight:700;font-size:10.5px;letter-spacing:.6px;color:var(--ink)}

  /* spine */
  .spine{position:absolute;left:574px;top:0;width:52px;height:866px}
  .spine-title{position:absolute;left:14px;top:34px;writing-mode:vertical-rl;font-family:"Oswald",sans-serif;font-weight:500;font-size:15px;letter-spacing:.5px;text-transform:uppercase;white-space:nowrap}
  .spine-title .gold{font-weight:600}
  .spine-mark{position:absolute;left:7px;top:410px;width:36px;height:36px;border:2px solid var(--gold);border-radius:50%}
  .spine-author{position:absolute;left:15px;top:540px;writing-mode:vertical-rl;font-family:"Montserrat",sans-serif;font-weight:700;font-size:15px;letter-spacing:7px;text-transform:uppercase;white-space:nowrap}

  /* front cover */
  .front .title-block{left:726px;width:360px;top:366px}
  .front .title-kicker{font-size:34px;letter-spacing:7px;line-height:34px}
  .front .title-main{font-size:214px;margin-top:4px}
  .front .title-tail{font-size:28px;letter-spacing:4px;line-height:30px;margin-top:2px}
  .subtitle{position:absolute;left:726px;width:360px;top:666px;text-align:center;font-family:"Montserrat",sans-serif;font-weight:400;font-size:12.4px;letter-spacing:3.6px;line-height:17px;text-transform:uppercase;color:var(--ink-soft)}
  .subtitle .ring{border:1px solid var(--ink-soft);border-radius:50%;padding:0 4px}
  .front-author{position:absolute;left:676px;width:460px;top:792px;text-align:center;font-family:"Montserrat",sans-serif;font-weight:700;font-size:20px;letter-spacing:9px;text-transform:uppercase;white-space:nowrap}
</style>
</head>
<body>
<div class="cover">
  <div class="athlete-photo" role="img" aria-label="Black and white photo of a female athlete in a dynamic leaping pose"></div>

  <section class="back">
    <div class="title-block">
      <div class="title-kicker">Growing Into a</div>
      <div class="title-main gold">Fearless</div>
      <div class="title-tail">Young Competitor</div>
    </div>
    <div class="blurb">
      <p><strong>Raising the Fearless Young Competitor</strong> is more than a book about training; it's a call to action for parents, coaches, and anyone who wants to see girls rise strong in sport and in life.</p>
      <p>Grounded in years of coaching experience and real conversations with athletes and parents, this book delivers practical, no-fluff guidance on what young female athletes truly need: smart nutrition, intentional recovery, habits of success, and a mindset that holds strong under pressure.</p>
      <p>Whether she's stepping onto the field for the first time or chasing down scholarships, this book equips you to lead her well at home, in the stands, and through every stage of her journey. Because being FEARLESS isn't just how she plays, it's about who she becomes.</p>
    </div>
    <div class="about-heading">About the author</div>
    <div class="author-photo" role="img" aria-label="Portrait photo of the author"></div>
    <div class="bio">
      <span class="wrap"></span>
      <p>Daniel Hartwell, CSCS, is the owner of Stride Performance Lab in Maple Falls, Ohio, where he's spent the last decade helping over 1,000 female athletes maximize performance, minimize injury risk, and build fearless confidence.</p>
      <p>A former collegiate athlete turned performance coach, Daniel's passion for training female athletes began after working with a young soccer player recovering from ACL surgery a moment that transformed his career and ignited a mission to change the way girls are trained and developed.</p>
      <p>Daniel believes every girl deserves the confidence to know she's capable, strong, and created with purpose. He is also an author and speaker, presenting to schools and companies, as well as at the Elevate Strength Coaching Summit, where he shares his expertise in developing strong, resilient female</p>
    </div>
    <div class="brand">
      <div class="brand-dot"></div>
      <div class="brand-name">FEARLESS COMPETITOR</div>
    </div>
  </section>

  <section class="spine">
    <div class="spine-title">Growing Into a <span class="gold">Fearless</span> Young Competitor</div>
    <div class="spine-mark"></div>
    <div class="spine-author">Daniel Hartwell</div>
  </section>

  <section class="front">
    <div class="title-block">
      <div class="title-kicker">Growing Into a</div>
      <div class="title-main gold">Fearless</div>
      <div class="title-tail">Young Competitor</div>
    </div>
    <div class="subtitle">The <span class="ring">Athlete</span> Blueprint for becoming strong, confident, and mentally tough in sports and life</div>
    <div class="front-author">Daniel Hartwell</div>
  </section>
</div>
</body>
</html>
```